Asia based real estate financing firm needs and AWESOME design for a biz card -Harbor Lending Circle

Looking for a stylish, & corporate-looking business card for a real estate financing brokerage firm in Asia, offering global mortgage loans. I uploaded our current logos. We would like to add a splash of color (perhaps the house icon) or any other suggestions are open. For the winning designer, we have a lot of work! Thanks and best of luck!

Target Market(s)

Real estate investors globally. We want to look more like a BANK and NOT a real estate company. Please don't play up on a "house" design.

Industry/Entity Type

Banking

Contact Information for Business Card

Harbor Lending Circle
Peter Wilks
Co-Founder | Partner

14 Cassia Lane, Suite 310
Singapore 047219
www.hlc-example.asia
peterwilks@hlc-example.asia
+65 555-0142
WeChat: peterwilks

Colors

Designer to choose colors to be used in the design.

Requirements
Must have
• Must have the standard business requirements for a card; name, address, email, etc
• Can be horizontal or vertical.
Nice to have
• It would be great to see some sort of variation to the logo with a pop of color. Red is good as we're in Asia, however, other options work as well.
• Our tag line is - Lending Without Limits. It doesn't have to be on the card but might be nice.
• I'd like to start seeing our tagline within the cards as well. - Lending Without Limits.
• Also, please add our location. The location for this card is Singapore so perhaps it can be highlighted or emphasised in some way.
• Singapore | Taipei | Seoul | Jakarta
• As we will soon open an office in Shanghai, having an option for both languages would be great.
Should not have
• I'm exceited and open to your creativity ... knock it out of the park!

```html
<!DOCTYPE html>
<html lang="en">
<head>
<meta charset="utf-8">
<title>Harbor Lending Circle – Business Card</title>
<link rel="stylesheet" href="https://fonts.googleapis.com/css2?family=Marcellus&family=Lato:wght@400;700&display=swap">
<style>
  :root {
    --brand-blue: #1560bd;
    --brand-blue-soft: #1a68c6;
    --band-white: #f4f4f4;
    --ink-white: #ffffff;
    --page-bg: #e6e7e9;
    --divider: rgba(255, 255, 255, 0.35);
  }
  * { box-sizing: border-box; margin: 0; padding: 0; }
  html, body { width: 1200px; height: 782px; overflow: hidden; }
  body {
    background: var(--page-bg);
    font-family: "Lato", sans-serif;
    display: flex;
    align-items: center;
    justify-content: center;
    gap: 40px;
  }
  .card {
    position: relative;
    width: 540px;
    height: 310px;
    background: var(--brand-blue);
    box-shadow: 0 6px 18px rgba(0, 0, 0, 0.18);
    overflow: hidden;
  }

  /* ---------- Front ---------- */
  .front__band {
    position: absolute; left: 0; right: 0; bottom: 0;
    height: 62px;
    background: var(--band-white);
    display: flex; align-items: center;
    padding-left: 62px;
  }
  .tagline {
    font-family: "Marcellus", serif;
    color: var(--brand-blue);
    font-size: 22px;
    letter-spacing: 1.5px;
    text-transform: uppercase;
  }
  .brand-name {
    position: absolute; left: 36px; top: 78px;
    width: 210px;
    font-family: "Marcellus", serif;
    color: var(--ink-white);
    font-size: 30px;
    line-height: 1.15;
  }
  .divider {
    position: absolute; left: 262px; top: 40px;
    width: 1px; height: 190px;
    background: var(--divider);
  }
  .contact {
    position: absolute; left: 284px; top: 42px;
    color: var(--ink-white);
  }
  .contact__name {
    font-family: "Marcellus", serif;
    font-size: 22px;
    letter-spacing: 1px;
    text-transform: uppercase;
    line-height: 1;
  }
  .contact__title { font-size: 15px; margin: 3px 0 6px; }
  .contact__list { list-style: none; font-size: 13.5px; line-height: 1.32; }
  .contact__list li { display: flex; align-items: center; gap: 6px; }
  .contact__list svg { width: 11px; height: 11px; flex: none; fill: var(--ink-white); }
  .contact__address { font-size: 13.5px; line-height: 1.32; }

  /* ---------- Back ---------- */
  .back__pattern {
    position: absolute; inset: 0 0 56px 0;
    background: linear-gradient(160deg, var(--brand-blue-soft), var(--brand-blue));
  }
  .back__mark {
    position: absolute; right: 150px; bottom: 70px;
    font-family: "Marcellus", serif;
    color: var(--ink-white);
    font-size: 15px;
  }
  .back__band {
    position: absolute; left: 0; right: 0; bottom: 0;
    height: 56px;
    background: var(--band-white);
    display: flex; align-items: center;
    padding-left: 92px;
  }
  .offices { color: var(--brand-blue); font-size: 16px; }
  .offices strong { font-weight: 700; }
</style>
</head>
<body>

  <section class="card card--front" aria-label="Business card front">
    <div class="brand-name">Harbor Lending Circle</div>
    <div class="divider"></div>
    <div class="contact">
      <p class="contact__name">Peter Wilks</p>
      <p class="contact__title">Co-Founder&nbsp;&nbsp;|&nbsp;&nbsp;Partner</p>
      <ul class="contact__list">
        <li><svg viewBox="0 0 12 12" aria-hidden="true"><path d="M2.5 1h2l1 3-1.3 1a6 6 0 0 0 2.8 2.8l1-1.3 3 1v2a1 1 0 0 1-1 1A9.5 9.5 0 0 1 1.5 2a1 1 0 0 1 1-1z"/></svg>+65 555-0142</li>
        <li><svg viewBox="0 0 12 12" aria-hidden="true"><path d="M1 2.5h10v7H1z M1 2.8l5 3.7 5-3.7" stroke="#1560bd" stroke-width="0.8"/></svg>peterwilks@hlc-example.asia</li>
        <li><svg viewBox="0 0 12 12" aria-hidden="true"><circle cx="6" cy="6" r="5"/><path d="M1 6h10M6 1c-2 2.5-2 7.5 0 10M6 1c2 2.5 2 7.5 0 10" stroke="#1560bd" stroke-width="0.7" fill="none"/></svg>www.hlc-example.asia</li>
        <li><svg viewBox="0 0 12 12" aria-hidden="true"><circle cx="6" cy="6" r="5"/></svg>peterwilks</li>
      </ul>
      <p class="contact__address">14 Cassia Lane, Suite 310<br>Singapore 047219</p>
    </div>
    <div class="front__band"><span class="tagline">Lending Without Limits</span></div>
  </section>

  <section class="card card--back" aria-label="Business card back">
    <div class="back__pattern" role="img" aria-label="Faint repeated brand-name pattern on blue"></div>
    <div class="back__mark">Harbor Lending Circle</div>
    <div class="back__band">
      <p class="offices"><strong>Singapore</strong> | Taipei | Seoul | Jakarta</p>
    </div>
  </section>

</body>
</html>
```